Junior Rugby Event needs 4 page Brochure

4 Page A4 brochure to be designed for a junior rugby event to be held in japan.. The brochure will entice coaches, teachers and players to the event.
The brochure will provide a basic overview of the event - dates, venue and promote some of the key features of the host, venue and event.
Event logo has been included. Design overview with copy has been included as word document. Images have been attached that can be used or alternatives sourced. A PDF document has been included of a design example that we like.
Rugby Clubs and Schools
Events

```html
<!DOCTYPE html>
<html lang="en">
<head>
<meta charset="utf-8">
<title>2019 Pacific Youth Rugby Classic – Brochure</title>
<link rel="stylesheet" href="https://fonts.googleapis.com/css2?family=Arvo:wght@400;700&family=Arimo:wght@400;700&display=swap">
<style>
  :root{
    --navy:#2b2f72;
    --grass-light:#c9d98a;
    --grass-mid:#a9c46a;
    --grass-deep:#6f9a3c;
    --chalk:#eef1e4;
    --stage:#8fcfa6;
    --red:#d7263d;
  }
  *{box-sizing:border-box;margin:0;padding:0}
  html,body{width:1200px;height:824px;overflow:hidden}
  body{background:var(--stage);font-family:"Arimo",Arial,sans-serif;color:var(--navy)}
  .spread{position:absolute;left:48px;top:22px;width:1104px;height:780px;display:flex;box-shadow:0 10px 30px rgba(0,0,0,.18)}
  .page{position:relative;width:552px;height:780px;overflow:hidden}
  .page__photo{position:absolute;inset:0;
    background:
      linear-gradient(115deg, transparent 38%, rgba(238,241,228,.75) 48%, rgba(238,241,228,.75) 52%, transparent 62%),
      linear-gradient(180deg,var(--grass-light) 0%,var(--grass-mid) 55%,var(--grass-deep) 100%);}
  .page--back .page__photo{background:
      linear-gradient(125deg, transparent 52%, rgba(238,241,228,.7) 62%, rgba(238,241,228,.7) 66%, transparent 76%),
      linear-gradient(180deg,var(--grass-light) 0%,var(--grass-mid) 50%,#8fb35a 100%);}
  .page__content{position:relative;z-index:1}

  /* back page */
  .back{padding:60px 44px 0 44px}
  .back h2{font-family:"Arvo",Georgia,serif;font-weight:700;font-size:22px;margin-bottom:12px}
  .back h3{font-family:"Arvo",Georgia,serif;font-weight:700;font-size:17px;margin:26px 0 8px}
  .back p{font-size:12.5px;line-height:1.45}
  .back ul{font-size:12.5px;line-height:1.5;padding-left:18px}
  .back .contact{position:absolute;left:44px;right:44px;top:680px;font-size:15px;line-height:1.35}

  /* front page */
  .frame{position:absolute;inset:30px;border:2px solid var(--navy)}
  .front{display:flex;flex-direction:column;align-items:center;text-align:center;padding-top:110px}
  .event-mark{display:flex;align-items:center;gap:12px;background:rgba(255,255,255,.85);padding:16px 22px}
  .event-mark__dot{width:22px;height:22px;border-radius:50%;background:var(--red)}
  .event-mark__name{font-family:"Arvo",Georgia,serif;font-weight:700;font-size:20px;color:var(--navy)}
  .front h1{font-family:"Arvo",Georgia,serif;font-weight:700;font-size:34px;line-height:1.2;margin-top:150px}
  .front .place{font-family:"Arvo",Georgia,serif;font-weight:700;font-size:22px;margin-top:26px}
  .front .dates{font-family:"Arvo",Georgia,serif;font-weight:700;font-size:17px;margin-top:6px}
  .front sup{font-size:.6em}
</style>
</head>
<body>
<div class="spread">
  <section class="page page--back">
    <div class="page__photo" role="img" aria-label="Close-up photograph of a rugby pitch with grass and a white chalk line"></div>
    <div class="page__content back">
      <h2>Travel &amp; Tournament Package</h2>
      <p>Our aim is to make participation in the Pacific Youth Rugby Classic as simple as possible for you, we therefore a number of different tournament packages. We also have a network of agents around the world who will assist you with flights and tour extension options.</p>

      <h3>Harbour Field Player Package</h3>
      <ul>
        <li>6 nights accommodation in Harbour Field Lodges, bunk rooms.</li>
        <li>Breakfast, Lunch and Dinner each day</li>
        <li>Airport or Train Station Transfers - one per team for arrival and departure.</li>
        <li>Tournament Entry (4 games guaranteed)</li>
        <li>Half Day Guided Fukuoka Sightseeing Tour including Kushida Shrine and Fukuoka Castle</li>
        <li>Exclusive Pacific Youth Rugby Classic Merchandise</li>
      </ul>

      <h3>Fukuoka Player or Supporter Package</h3>
      <ul>
        <li>6 nights hotel accommodation in Fukuoka City.</li>
        <li>Breakfast daily</li>
        <li>Airport or Train Station Transfers - one per team for arrival and departure.</li>
        <li>Tournament Return Shuttle Service</li>
        <li>Tournament Entry (4 games guaranteed)</li>
        <li>Half Day Guided Fukuoka Sightseeing Tour including Kushida Shrine and Fukuoka Castle</li>
        <li>Exclusive Pacific Youth Rugby Classic Merchandise</li>
      </ul>

      <p class="contact">Please contact us to receive a tailored quote for your team for the Pacific Youth Rugby Classic. info@pacificyouthrugbyclassic.com</p>
    </div>
  </section>

  <section class="page page--front">
    <div class="page__photo" role="img" aria-label="Photograph of a rugby pitch with grass and a white chalk line"></div>
    <div class="frame"></div>
    <div class="page__content front">
      <div class="event-mark">
        <span class="event-mark__dot"></span>
        <span class="event-mark__name">Pacific Youth Rugby Classic</span>
      </div>
      <h1>2019 Pacific Youth<br>Rugby Classic</h1>
      <p class="place">Fukuoka, Japan</p>
      <p class="dates">30<sup>th</sup> September - 4<sup>th</sup> October 2019</p>
    </div>
  </section>
</div>
</body>
</html>
```